Velmarine - Mechanic/Collision Center Business Card

We're looking for a business card design for our mechanic/ collision repair shop.

Can be with colours or monochromatic.

See the attached files.

Many thanks

```html
<!DOCTYPE html>
<html lang="pt">
<head>
<meta charset="utf-8">
<title>Velmarine – Cartão de visita</title>
<link rel="stylesheet" href="https://fonts.googleapis.com/css2?family=Roboto:wght@400;500;700;900&display=swap">
<style>
  :root {
    --ink: #1c1f22;
    --blue: #1e9cd7;
    --grey: #7a7b7f;
    --ghost: #f1f2f3;
    --paper: #ffffff;
  }
  html, body { margin: 0; padding: 0; overflow: hidden; background: var(--paper); }
  .card {
    position: relative;
    width: 1200px;
    height: 686px;
    overflow: hidden;
    background: var(--paper);
    font-family: "Roboto", Arial, sans-serif;
  }
  .card-art { position: absolute; inset: 0; }
  .ghost-word {
    font-family: "Roboto", Arial, sans-serif;
    font-weight: 900;
    font-size: 230px;
    fill: var(--ghost);
  }
  .brand {
    position: absolute;
    left: 62px;
    top: 196px;
    width: 440px;
    display: flex;
    align-items: center;
    justify-content: center;
    gap: 16px;
  }
  .brand-mark {
    width: 34px;
    height: 34px;
    background: var(--blue);
  }
  .brand-name {
    font-weight: 900;
    font-size: 56px;
    letter-spacing: 1px;
    color: var(--ink);
    line-height: 1;
  }
  .person-name {
    position: absolute;
    left: 692px;
    top: 146px;
    width: 420px;
    text-align: center;
    margin: 0;
    font-weight: 700;
    font-size: 52px;
    color: var(--paper);
    line-height: 1;
    white-space: nowrap;
  }
  .contact-list {
    position: absolute;
    left: 0;
    top: 0;
    margin: 0;
    padding: 0;
    list-style: none;
  }
  .contact-item {
    position: absolute;
    left: 149px;
    font-size: 22px;
    color: var(--paper);
    white-space: nowrap;
    line-height: 1;
  }
  .contact-phone { top: 329px; }
  .contact-mail  { top: 371px; }
  .contact-web   { top: 412px; }
  .contact-city  { top: 469px; }
  .street {
    position: absolute;
    left: 179px;
    top: 570px;
    margin: 0;
    font-size: 40px;
    color: var(--ink);
    line-height: 1;
    white-space: nowrap;
  }
  .company-legal {
    position: absolute;
    left: 834px;
    top: 571px;
    margin: 0;
    font-weight: 700;
    font-size: 30px;
    color: var(--blue);
    line-height: 1;
    white-space: nowrap;
  }
</style>
</head>
<body>
<main class="card">
  <svg class="card-art" width="1200" height="686" viewBox="0 0 1200 686" aria-hidden="true">
    <!-- faint background wordmark -->
    <text class="ghost-word" x="640" y="690">VELMA</text>

    <!-- grey bands behind the name plate -->
    <polygon fill="var(--grey)" points="741,0 1200,0 1200,97 777,97"/>
    <polygon fill="var(--grey)" points="840,251 1200,251 1200,322 869,322"/>

    <!-- name plate -->
    <polygon fill="var(--blue)" points="663,97 1072,97 1131,251 722,251"/>

    <!-- dark contact panel -->
    <polygon fill="var(--ink)" points="0,303 546,303 697,686 0,686"/>

    <!-- contact row rules -->
    <g fill="var(--blue)">
      <rect x="0" y="336" width="66" height="5"/>
      <rect x="0" y="380" width="66" height="5"/>
      <rect x="0" y="422" width="66" height="5"/>
      <rect x="0" y="478" width="66" height="5"/>
    </g>

    <!-- phone icon -->
    <g transform="translate(110,338)">
      <circle r="12" fill="var(--blue)"/>
      <path d="M-5,-6 l3,-1 2,4 -2,2 q1.5,3 4.5,4.5 l2,-2 4,2 -1,3 q-8,0 -12.5,-12.5z" fill="var(--paper)"/>
    </g>
    <!-- mail icon -->
    <g transform="translate(110,381)">
      <circle r="12" fill="var(--blue)"/>
      <rect x="-6.5" y="-4.5" width="13" height="9" fill="var(--paper)"/>
      <polyline points="-6.5,-4.5 0,1 6.5,-4.5" fill="none" stroke="var(--blue)" stroke-width="1.4"/>
    </g>
    <!-- web icon (plain circle) -->
    <g transform="translate(110,424)">
      <circle r="12" fill="var(--blue)"/>
    </g>
    <!-- house icon -->
    <g transform="translate(110,480)">
      <polygon points="0,-13 12,-3 -12,-3" fill="var(--blue)"/>
      <rect x="-8" y="-3" width="16" height="14" fill="var(--blue)"/>
      <rect x="-2.5" y="3" width="5" height="8" fill="var(--ink)"/>
    </g>

    <!-- address band -->
    <polygon fill="var(--blue)" points="0,544 786,544 686,629 0,629"/>
    <rect x="0" y="587" width="70" height="5" fill="var(--ink)"/>
    <circle cx="121" cy="589" r="34" fill="var(--ink)"/>
    <path d="M121,608 q-13,-15 -13,-24 a13,13 0 0 1 26,0 q0,9 -13,24z" fill="var(--blue)"/>
    <circle cx="121" cy="583" r="5" fill="var(--ink)"/>

    <!-- legal name rule -->
    <rect x="1146" y="583" width="54" height="5" fill="var(--blue)"/>
  </svg>

  <div class="brand">
    <span class="brand-mark"></span>
    <span class="brand-name">VELMARINE</span>
  </div>

  <h1 class="person-name">TOMÉ VARZELO</h1>

  <ul class="contact-list">
    <li class="contact-item contact-phone">+351 210000482 / +351 910000735</li>
    <li class="contact-item contact-mail">velmarine.oficina@mail.pt</li>
    <li class="contact-item contact-web">www.velmarine-auto.pt</li>
    <li class="contact-item contact-city">1950-118 Lisboa</li>
  </ul>

  <p class="street">Rua das Amoreiras, 41</p>

  <p class="company-legal">VELMARINE, LDA</p>
</main>
</body>
</html>
```